Powerpoint Slide Deck

I had my logo designed using drafthollow and would like to have a professional looking powerpoint deck created with my logo etc. my website is vantreo.info

```html
<!DOCTYPE html>
<html lang="en">
<head>
<meta charset="utf-8">
<title>Vantreo Presentation Deck</title>
<link href="https://fonts.googleapis.com/css2?family=Raleway:wght@300;400;500;600;700;800&display=swap" rel="stylesheet">
<style>
  :root {
    --canvas: #e3e3e8;
    --hero-bg: #d9dbe2;
    --white: #ffffff;
    --ink: #3a4348;
    --ink-soft: #6b7075;
    --grey-line: #d8d8dc;
    --grey-fill: #f0f0f2;
    --purple-deep: #5a3fc9;
    --purple-mid: #7b52d6;
    --purple-soft: #a877d8;
    --blue: #5b4fd6;
    --violet: #a34cc7;
    --red: #e8222d;
    --green: #5fd35c;
    --lime: #a8c43a;
    --leaf: #3fae3f;
    --teal: #3aa57c;
    --table-dark: #3f3f3f;
    --table-green: #4fd35a;
  }
  * { box-sizing: border-box; margin: 0; padding: 0; }
  html, body { width: 1200px; height: 2459px; overflow: hidden; }
  body {
    position: relative;
    background: var(--canvas);
    font-family: "Raleway", sans-serif;
    color: var(--ink);
  }
  .hero {
    position: absolute; left: 0; top: 0; width: 1200px; height: 740px;
    background: var(--hero-bg);
  }
  .hero .brand-mark {
    position: absolute; right: 40px; top: 120px;
    display: flex; align-items: center; gap: 14px;
    font-size: 52px; font-weight: 600; color: var(--ink); letter-spacing: 1px;
  }
  .brand-mark .dot {
    width: 26px; height: 26px; border-radius: 50%; background: var(--purple-mid);
  }
  .hero-slide-holder {
    position: absolute; left: 50px; top: 130px;
    width: 563px; height: 316px;
    transform: scale(1.42); transform-origin: top left;
    box-shadow: 0 4px 14px rgba(0,0,0,.12);
  }

  .slide {
    position: absolute; width: 563px; height: 316px;
    background: var(--white); overflow: hidden;
  }
  .hero-slide-holder .slide { left: 0; top: 0; }
  .col-a { left: 28px; } .col-b { left: 609px; }
  .row-1 { top: 768px; } .row-2 { top: 1103px; } .row-3 { top: 1438px; }
  .row-4 { top: 1773px; } .row-5 { top: 2108px; }

  .abs { position: absolute; }
  .placeholder { position: absolute; }

  /* footer */
  .mini-logo {
    position: absolute; left: 16px; top: 277px;
    font-size: 12px; font-weight: 600; color: var(--ink);
  }
  .footer-bar {
    position: absolute; left: 72px; top: 288px; width: 475px; height: 11px;
    border-radius: 6px;
    background: linear-gradient(90deg, #c886d8, #9a62d8 55%, #6f4fd6);
  }
  .footer-bar span {
    position: absolute; right: 22px; top: 2px;
    font-size: 4.5px; color: var(--white); font-weight: 500;
  }
  .page-no {
    position: absolute; right: -1px; top: -1px; width: 13px; height: 13px;
    border-radius: 50%; background: var(--white); border: 1.5px solid #6f4fd6;
    font-size: 6px; font-weight: 700; color: #6f4fd6;
    display: flex; align-items: center; justify-content: center;
  }

  /* title slide */
  .title-band { position: absolute; left: 0; top: 32px; width: 563px; height: 252px; }
  .title-logo {
    position: absolute; left: 40px; top: 36px;
    font-size: 19px; font-weight: 600; color: var(--ink);
  }
  .title-text {
    position: absolute; left: 58px; top: 120px;
    font-size: 27px; line-height: 1.12; font-weight: 800; color: var(--white); letter-spacing: .3px;
  }
  .title-sub {
    position: absolute; left: 58px; top: 186px;
    font-size: 11.5px; font-weight: 400; color: var(--white);
  }
  .title-date {
    position: absolute; left: 58px; top: 222px;
    border: 1px solid var(--white); border-radius: 3px;
    padding: 3px 12px; font-size: 6px; letter-spacing: 1.4px; color: var(--white); font-weight: 600;
  }
  .slide-copy {
    position: absolute; left: 0; width: 100%; text-align: center;
    font-size: 5px; color: #9a9a9f;
  }

  /* headings */
  .heading {
    position: absolute; left: 0; width: 100%; text-align: center;
    font-size: 19px; font-weight: 300; color: var(--ink);
  }
  .heading b, .side-heading b, .item-heading b { font-weight: 700; }
  .side-heading { position: absolute; font-size: 19px; font-weight: 300; color: var(--ink); }
  .body-text { position: absolute; font-size: 8px; line-height: 1.22; color: var(--ink-soft); }
  .body-text p + p { margin-top: 7px; }
  .item { position: absolute; text-align: center; }
  .item-heading { font-size: 10px; font-weight: 300; color: var(--ink); }
  .item-text { margin-top: 12px; font-size: 6.3px; line-height: 1.2; color: var(--ink-soft); }
  .label { position: absolute; width: 130px; }
  .label.right { text-align: right; }
  .label .t { font-size: 9px; font-weight: 300; color: var(--ink); }
  .label .t b { font-weight: 700; }
  .label .d { margin-top: 3px; font-size: 5.8px; line-height: 1.2; color: var(--ink-soft); }

  /* table */
  .data-table {
    position: absolute; left: 32px; top: 78px; width: 528px;
    border-collapse: collapse; font-size: 6px; color: var(--ink);
  }
  .data-table th {
    height: 26px; color: var(--white); font-weight: 600; font-size: 7px; line-height: 1.1;
  }
  .data-table th small { display: block; font-weight: 400; font-size: 6.5px; }
  .data-table th.first { background: var(--table-dark); text-align: left; padding-left: 5px; width: 162px; }
  .data-table th.c1 { background: var(--blue); }
  .data-table th.c2 { background: var(--violet); }
  .data-table th.c3 { background: var(--red); }
  .data-table th.c4 { background: var(--table-green); }
  .data-table td { height: 23px; text-align: center; border-bottom: 1px solid #ececef; color: var(--ink-soft); }
  .data-table td.name { text-align: left; padding-left: 5px; font-weight: 600; color: var(--ink); }
  .data-table td.hi { color: var(--blue); font-weight: 700; }
  .data-table tr:nth-child(even) td { background: #f6f6f8; }
  .col-highlight {
    position: absolute; left: 193px; top: 74px; width: 91px; height: 210px;
    border: 1.6px solid var(--blue); border-radius: 5px;
  }

  /* thank you */
  .thanks-title { position: absolute; left: 60px; top: 90px; font-size: 27px; font-weight: 300; color: var(--white); }
  .contact-head { position: absolute; left: 60px; top: 160px; font-size: 11px; font-weight: 700; color: var(--white); }
  .contact-list { position: absolute; left: 60px; top: 186px; list-style: none; }
  .contact-list li {
    display: flex; align-items: center; gap: 8px; height: 17px;
    font-size: 7.5px; color: var(--white);
  }
  .contact-list svg { width: 10px; height: 10px; }
  .thanks-logo { position: absolute; right: 26px; top: 48px; font-size: 19px; font-weight: 600; color: var(--ink); }
</style>
</head>
<body>

<svg width="0" height="0" style="position:absolute" aria-hidden="true">
  <defs>
    <linearGradient id="band-grad" x1="0" y1="0" x2="1" y2="0">
      <stop offset="0" stop-color="#5a3fc9"/>
      <stop offset="1" stop-color="#9c6ed8"/>
    </linearGradient>
    <symbol id="i-cloud" viewBox="0 0 24 24"><path fill="currentColor" d="M7 18h10a4 4 0 0 0 .5-7.970A6 6 0 0 0 6.1 11.1 3.5 3.5 0 0 0 7 18z"/></symbol>
    <symbol id="i-monitor" viewBox="0 0 24 24"><path fill="currentColor" fill-rule="evenodd" d="M3 4h18v12H3z M5 6v8h14V6z"/><rect x="10" y="16" width="4" height="3" fill="currentColor"/><rect x="7" y="19" width="10" height="1.6" fill="currentColor"/></symbol>
    <symbol id="i-gear" viewBox="0 0 24 24"><circle cx="12" cy="12" r="7.5" fill="none" stroke="currentColor" stroke-width="4" stroke-dasharray="3 2.9"/><circle cx="12" cy="12" r="5.2" fill="none" stroke="currentColor" stroke-width="2"/></symbol>
    <symbol id="i-bulb" viewBox="0 0 24 24"><circle cx="12" cy="10" r="6" fill="currentColor"/><rect x="9.5" y="15" width="5" height="5" rx="1" fill="currentColor"/></symbol>
    <symbol id="i-search" viewBox="0 0 24 24"><circle cx="10" cy="10" r="6" fill="none" stroke="currentColor" stroke-width="2.6"/><path d="M14.5 14.5 20 20" stroke="currentColor" stroke-width="3.2" stroke-linecap="round"/></symbol>
    <symbol id="i-people" viewBox="0 0 24 24"><circle cx="6" cy="9" r="2.5" fill="currentColor"/><circle cx="18" cy="9" r="2.5" fill="currentColor"/><circle cx="12" cy="8" r="3.5" fill="currentColor"/><path d="M5 19a7 6 0 0 1 14 0z" fill="currentColor"/><path d="M1 17a5 4.5 0 0 1 6-3.5 6 6 0 0 0-2 3.5z M23 17a5 4.5 0 0 0-6-3.5 6 6 0 0 1 2 3.5z" fill="currentColor"/></symbol>
    <symbol id="i-chart" viewBox="0 0 24 24"><rect x="4" y="14" width="3.5" height="6" fill="currentColor"/><rect x="10" y="10" width="3.5" height="10" fill="currentColor"/><rect x="16" y="6" width="3.5" height="14" fill="currentColor"/><path d="M4 11 11 6l3 2 5-5" stroke="currentColor" stroke-width="1.6" fill="none"/></symbol>
    <symbol id="i-phone" viewBox="0 0 24 24"><path fill="currentColor" d="M6.6 10.8a15 15 0 0 0 6.6 6.6l2.2-2.2a1 1 0 0 1 1-.25 11.4 11.4 0 0 0 3.6.57 1 1 0 0 1 1 1V20a1 1 0 0 1-1 1A17 17 0 0 1 3 4a1 1 0 0 1 1-1h3.5a1 1 0 0 1 1 1c0 1.250.2 2.450.57 3.570a1 1 0 0 1-.25 1z"/></symbol>
    <symbol id="i-at" viewBox="0 0 24 24"><circle cx="12" cy="12" r="4" fill="none" stroke="currentColor" stroke-width="2.2"/><path d="M16 8v5.5a2.5 2.5 0 0 0 5 0V12a9 9 0 1 0-3.5 7.1" fill="none" stroke="currentColor" stroke-width="2.2"/></symbol>
    <symbol id="i-globe" viewBox="0 0 24 24"><g fill="none" stroke="currentColor" stroke-width="1.8"><circle cx="12" cy="12" r="9"/><ellipse cx="12" cy="12" rx="4" ry="9"/><path d="M3 12h18M5 7h14M5 17h14"/></g></symbol>
  </defs>
</svg>

<!-- Hero area -->
<section class="hero">
  <div class="hero-slide-holder">
    <div class="slide title-slide">
      <svg class="title-band" viewBox="0 0 563 252" preserveAspectRatio="none" role="img" aria-label="Photo of two IT engineers with a laptop in a server room, tinted purple">
        <polygon points="0,48 140,48 195,0 563,0 563,252 0,252" fill="url(#band-grad)"/>
        <polygon points="290,0 563,0 563,252 330,252" fill="#b08de0" opacity=".25"/>
      </svg>
      <div class="title-logo">Vantreo</div>
      <div class="title-text">PRESENTATION<br>TITLE GOES HERE!</div>
      <div class="title-sub">Sub Title of Presentation Goes Here</div>
      <div class="title-date">February 16, 2023</div>
      <div class="slide-copy" style="top:300px">Copyright © 2022 Vantreo All rights reserved</div>
    </div>
  </div>
  <div class="brand-mark"><span class="dot"></span>Vantreo</div>
</section>

<!-- Slide 1: title -->
<div class="slide col-a row-1">
  <svg class="title-band" viewBox="0 0 563 252" preserveAspectRatio="none" role="img" aria-label="Photo of two IT engineers with a laptop in a server room, tinted purple">
    <polygon points="0,48 140,48 195,0 563,0 563,252 0,252" fill="url(#band-grad)"/>
    <polygon points="290,0 563,0 563,252 330,252" fill="#b08de0" opacity=".25"/>
  </svg>
  <div class="title-logo">Vantreo</div>
  <div class="title-text">PRESENTATION<br>TITLE GOES HERE!</div>
  <div class="title-sub">Sub Title of Presentation Goes Here</div>
  <div class="title-date">February 16, 2023</div>
  <div class="slide-copy" style="top:300px">Copyright © 2022 Vantreo All rights reserved</div>
</div>

<!-- Slide 2: about -->
<div class="slide col-b row-1">
  <div class="placeholder" role="img" aria-label="Illustration of people working around a large laptop with code and cloud icons"
       style="left:40px;top:55px;width:250px;height:185px;border-radius:10px;background:linear-gradient(135deg,#eef2fb,#cfe0f7 55%,#e9f3e6);"></div>
  <div class="side-heading" style="left:330px;top:82px">About <b>Vantreo</b></div>
  <div class="body-text" style="left:305px;top:126px;width:205px">
    <p>In a complex world of IT, Vantreo will assist you in optimizing IT spend. Our 20 plus years in the IT industry brings best of breed personnel from Data center, Managed Services, and Disaster Recovery, to help you get the best solutions for the best price.</p>
    <p>Let us help you simplify.</p>
  </div>
  <div class="mini-logo">Vantreo</div>
  <div class="footer-bar"><span>Copyright © 2022 Vantreo All rights reserved</span><b class="page-no">2</b></div>
</div>

<!-- Slide 3: why -->
<div class="slide col-a row-2">
  <div class="side-heading" style="left:84px;top:57px">Why <b>Vantreo</b></div>
  <div class="body-text" style="left:60px;top:101px;width:292px">
    <p>It's Simple. Our resources have years of experience understanding IT environments. All of our staff have been top of their class in each of their specialties and can help you optimize your spend with best of breed solutioning.</p>
    <p>Our staff have unmatched knowledge in Networking, Security, Data Center, Disaster Recovery, Orvane Solutions, Hyperscaler Solutions, Managed Services, and more. The people we put in front of you are the best of the best in IT.</p>
    <p>Its hard to find a great mechanic that you trust has your best interests in mind – its even harder to find a great IT specialist.</p>
    <p>Let our team help you optimize your environment.</p>
  </div>
  <div class="placeholder" role="img" aria-label="Photo of hands typing on a laptop at an office desk with a coffee mug and books"
       style="left:380px;top:5px;width:128px;height:252px;background:linear-gradient(160deg,#5b6a7c,#c9ccd1 45%,#3c3f45);"></div>
  <div class="mini-logo">Vantreo</div>
  <div class="footer-bar"><span>Copyright © 2022 Vantreo All rights reserved</span><b class="page-no">3</b></div>
</div>

<!-- Slide 4: solutions -->
<div class="slide col-b row-2">
  <div class="heading" style="top:26px">Our <b>Solutions</b></div>
  <svg class="abs" style="left:0;top:0" width="563" height="316" aria-hidden="true">
    <circle cx="128" cy="130" r="28" fill="var(--blue)"/>
    <circle cx="282" cy="130" r="28" fill="var(--violet)"/>
    <circle cx="435" cy="130" r="28" fill="var(--red)"/>
    <use href="#i-cloud" x="116" y="118" width="24" height="24" color="#fff"/>
    <use href="#i-monitor" x="270" y="118" width="24" height="24" color="#fff"/>
    <use href="#i-gear" x="423" y="118" width="24" height="24" color="#fff"/>
  </svg>
  <div class="item" style="left:68px;top:170px;width:120px">
    <div class="item-heading"><b>Heading</b> Goes Here</div>
    <div class="item-text">Lorem ipsum dolor sit amet, consectetur adipiscing elit. Vivamus eu dui ex. Curabitur dapibus dignissim dui, in molestie metus feugiat sed.</div>
  </div>
  <div class="item" style="left:222px;top:170px;width:120px">
    <div class="item-heading"><b>Heading</b> Goes Here</div>
    <div class="item-text">Lorem ipsum dolor sit amet, consectetur adipiscing elit. Vivamus eu dui ex. Curabitur dapibus dignissim dui, in molestie metus feugiat sed.</div>
  </div>
  <div class="item" style="left:375px;top:170px;width:120px">
    <div class="item-heading"><b>Heading</b> Goes Here</div>
    <div class="item-text">Lorem ipsum dolor sit amet, consectetur adipiscing elit. Vivamus eu dui ex. Curabitur dapibus dignissim dui, in molestie metus feugiat sed.</div>
  </div>
  <div class="mini-logo">Vantreo</div>
  <div class="footer-bar"><span>Copyright © 2022 Vantreo All rights reserved</span><b class="page-no">4</b></div>
</div>

<!-- Slide 5: hub -->
<div class="slide col-a row-3">
  <div class="heading" style="top:26px"><b>Heading</b> Goes Here</div>
  <svg class="abs" style="left:0;top:0" width="563" height="316" aria-hidden="true">
    <circle cx="295" cy="172" r="82" fill="none" stroke="#c9c9cf" stroke-width="1" stroke-dasharray="3 3"/>
    <circle cx="295" cy="172" r="52" fill="var(--grey-fill)"/>
    <circle cx="236" cy="113" r="16" fill="var(--blue)"/>
    <circle cx="354" cy="113" r="16" fill="var(--violet)"/>
    <circle cx="236" cy="231" r="16" fill="var(--green)"/>
    <circle cx="354" cy="231" r="16" fill="var(--red)"/>
    <use href="#i-bulb" x="228" y="105" width="16" height="16" color="#fff"/>
    <use href="#i-gear" x="346" y="105" width="16" height="16" color="#fff"/>
    <use href="#i-cloud" x="228" y="223" width="16" height="16" color="#fff"/>
    <use href="#i-monitor" x="346" y="223" width="16" height="16" color="#fff"/>
  </svg>
  <div class="label right" style="left:70px;top:90px"><div class="t"><b>Heading</b> Goes Here</div><div class="d">Adipiscing Elit. Vivamus Eu Dui Ex. Curabitur Dapibus Dignissim Dui, In Molestie Metus Feugiat Sed.</div></div>
  <div class="label" style="left:372px;top:90px"><div class="t"><b>Heading</b> Goes Here</div><div class="d">Adipiscing Elit. Vivamus Eu Dui Ex. Curabitur Dapibus Dignissim Dui, In Molestie Metus Feugiat Sed.</div></div>
  <div class="label right" style="left:70px;top:201px"><div class="t"><b>Heading</b> Goes Here</div><div class="d">Adipiscing Elit. Vivamus Eu Dui Ex. Curabitur Dapibus Dignissim Dui, In Molestie Metus Feugiat Sed.</div></div>
  <div class="label" style="left:372px;top:201px"><div class="t"><b>Heading</b> Goes Here</div><div class="d">Adipiscing Elit. Vivamus Eu Dui Ex. Curabitur Dapibus Dignissim Dui, In Molestie Metus Feugiat Sed.</div></div>
  <div class="mini-logo">Vantreo</div>
  <div class="footer-bar"><span>Copyright © 2022 Vantreo All rights reserved</span><b class="page-no">5</b></div>
</div>

<!-- Slide 6: segmented arc -->
<div class="slide col-b row-3">
  <div class="heading" style="top:26px"><b>Heading</b> Goes Here</div>
  <svg class="abs" style="left:0;top:0" width="563" height="316" aria-hidden="true">
    <g stroke="#fff" stroke-width="3">
      <path d="M213.7 269.3A115 115 0 0 1 180 188L243 188A52 52 0 0 0 258.2 224.8Z" fill="var(--blue)"/>
      <path d="M180 188A115 115 0 0 1 213.7 106.7L258.2 151.2A52 52 0 0 0 243 188Z" fill="var(--violet)"/>
      <path d="M213.7 106.7A115 115 0 0 1 295 73L295 136A52 52 0 0 0 258.2 151.2Z" fill="var(--red)"/>
      <path d="M295 73A115 115 0 0 1 376.3 106.7L331.8 151.2A52 52 0 0 0 295 136Z" fill="var(--lime)"/>
      <path d="M376.3 106.7A115 115 0 0 1 410 188L347 188A52 52 0 0 0 331.8 151.2Z" fill="var(--leaf)"/>
      <path d="M410 188A115 115 0 0 1 376.3 269.3L331.8 224.8A52 52 0 0 0 347 188Z" fill="var(--teal)"/>
    </g>
    <use href="#i-bulb" x="205" y="208" width="24" height="24" color="#fff"/>
    <use href="#i-search" x="205" y="144" width="24" height="24" color="#fff"/>
    <use href="#i-people" x="251" y="98" width="24" height="24" color="#fff"/>
    <use href="#i-monitor" x="315" y="98" width="24" height="24" color="#fff"/>
    <use href="#i-cloud" x="361" y="144" width="24" height="24" color="#fff"/>
    <use href="#i-chart" x="361" y="208" width="24" height="24" color="#fff"/>
    <g stroke="var(--red)" stroke-width="1" fill="var(--red)">
      <line x1="182" y1="70" x2="232" y2="70"/><circle cx="182" cy="70" r="1.8"/>
      <line x1="152" y1="137" x2="172" y2="137"/><circle cx="152" cy="137" r="1.8"/>
      <line x1="158" y1="204" x2="178" y2="204"/><circle cx="158" cy="204" r="1.8"/>
    </g>
    <g stroke="var(--lime)" stroke-width="1" fill="var(--lime)">
      <line x1="355" y1="70" x2="405" y2="70"/><circle cx="405" cy="70" r="1.8"/>
    </g>
    <g stroke="var(--leaf)" stroke-width="1" fill="var(--leaf)">
      <line x1="415" y1="137" x2="435" y2="137"/><circle cx="435" cy="137" r="1.8"/>
    </g>
    <g stroke="var(--teal)" stroke-width="1" fill="var(--teal)">
      <line x1="411" y1="204" x2="431" y2="204"/><circle cx="431" cy="204" r="1.8"/>
    </g>
  </svg>
  <div class="label right" style="left:48px;top:65px"><div class="t"><b>Title</b> Goes Here</div><div class="d">Adipiscing Elit. Vivamus Eu Dui Ex. Curabitur Dapibus Dignissim Dui, In Molestie.</div></div>
  <div class="label right" style="left:18px;top:132px"><div class="t"><b>Title</b> Goes Here</div><div class="d">Adipiscing Elit. Vivamus Eu Dui Ex. Curabitur Dapibus Dignissim Dui, In Molestie.</div></div>
  <div class="label right" style="left:24px;top:199px"><div class="t"><b>Title</b> Goes Here</div><div class="d">Adipiscing Elit. Vivamus Eu Dui Ex. Curabitur Dapibus Dignissim Dui, In Molestie.</div></div>
  <div class="label" style="left:410px;top:65px;width:120px"><div class="t"><b>Title</b> Goes Here</div><div class="d">Adipiscing Elit. Vivamus Eu Dui Ex. Curabitur Dapibus Dignissim Dui, In Molestie.</div></div>
  <div class="label" style="left:440px;top:132px;width:110px"><div class="t"><b>Title</b> Goes Here</div><div class="d">Adipiscing Elit. Vivamus Eu Dui Ex. Curabitur Dapibus Dignissim Dui, In Molestie.</div></div>
  <div class="label" style="left:436px;top:199px;width:110px"><div class="t"><b>Title</b> Goes Here</div><div class="d">Adipiscing Elit. Vivamus Eu Dui Ex. Curabitur Dapibus Dignissim Dui, In Molestie.</div></div>
  <div class="mini-logo">Vantreo</div>
  <div class="footer-bar"><span>Copyright © 2022 Vantreo All rights reserved</span><b class="page-no">6</b></div>
</div>

<!-- Slide 7: progress rings -->
<div class="slide col-a row-4">
  <div class="heading" style="top:26px"><b>Heading</b> Goes Here</div>
  <svg class="abs" style="left:0;top:0" width="563" height="316" aria-hidden="true">
    <g fill="none" stroke-width="6">
      <circle cx="125" cy="142" r="55" stroke="#efeff2" stroke-width="2"/>
      <circle cx="125" cy="142" r="55" stroke="var(--blue)" stroke-dasharray="221.2 345.6" transform="rotate(-90 125 142)"/>
      <circle cx="282" cy="142" r="55" stroke="#efeff2" stroke-width="2"/>
      <circle cx="282" cy="142" r="55" stroke="var(--violet)" stroke-dasharray="283.4 345.6" transform="rotate(-90 282 142)"/>
      <circle cx="439" cy="142" r="55" stroke="#efeff2" stroke-width="2"/>
      <circle cx="439" cy="142" r="55" stroke="var(--red)" stroke-dasharray="324.9 345.6" transform="rotate(-90 439 142)"/>
    </g>
    <g font-family="Raleway, sans-serif" font-size="19" font-weight="300" text-anchor="middle">
      <text x="125" y="149" fill="var(--blue)">64<tspan font-size="8">%</tspan></text>
      <text x="282" y="149" fill="var(--violet)">82<tspan font-size="8">%</tspan></text>
      <text x="439" y="149" fill="var(--red)">94<tspan font-size="8">%</tspan></text>
    </g>
  </svg>
  <div class="item" style="left:65px;top:214px;width:120px">
    <div class="item-heading"><b>Heading</b> Goes Here</div>
    <div class="item-text" style="margin-top:5px">Lorem ipsum dolor sit amet, consectetur adipiscing elit. Vivamus eu dui ex. Curabitur dapibus dignissim dui.</div>
  </div>
  <div class="item" style="left:222px;top:214px;width:120px">
    <div class="item-heading"><b>Heading</b> Goes Here</div>
    <div class="item-text" style="margin-top:5px">Lorem ipsum dolor sit amet, consectetur adipiscing elit. Vivamus eu dui ex. Curabitur dapibus dignissim dui.</div>
  </div>
  <div class="item" style="left:379px;top:214px;width:120px">
    <div class="item-heading"><b>Heading</b> Goes Here</div>
    <div class="item-text" style="margin-top:5px">Lorem ipsum dolor sit amet, consectetur adipiscing elit. Vivamus eu dui ex. Curabitur dapibus dignissim dui.</div>
  </div>
  <div class="mini-logo">Vantreo</div>
  <div class="footer-bar"><span>Copyright © 2022 Vantreo All rights reserved</span><b class="page-no">7</b></div>
</div>

<!-- Slide 8: bar charts -->
<div class="slide col-b row-4">
  <div class="heading" style="top:26px"><b>Heading</b> Goes Here</div>
  <svg class="abs" style="left:0;top:0" width="563" height="316" aria-hidden="true" font-family="Raleway, sans-serif" font-size="5.5" fill="#6b7075">
    <g stroke="#e4e4e8" stroke-width=".6">
      <line x1="86" y1="88" x2="86" y2="180"/><line x1="111.2" y1="88" x2="111.2" y2="180"/><line x1="136.4" y1="88" x2="136.4" y2="180"/><line x1="161.6" y1="88" x2="161.6" y2="180"/><line x1="186.8" y1="88" x2="186.8" y2="180"/><line x1="212" y1="88" x2="212" y2="180"/><line x1="237.2" y1="88" x2="237.2" y2="180"/><line x1="262.4" y1="88" x2="262.4" y2="180"/>
    </g>
    <g text-anchor="end">
      <text x="80" y="101">Category 4</text><text x="80" y="124">Category 3</text><text x="80" y="147">Category 2</text><text x="80" y="170">Category 1</text>
    </g>
    <rect x="86" y="96" width="55" height="7" fill="var(--blue)"/><rect x="141" y="96" width="22" height="7" fill="var(--violet)"/><rect x="163" y="96" width="61" height="7" fill="var(--red)"/>
    <rect x="86" y="119" width="44" height="7" fill="var(--blue)"/><rect x="130" y="119" width="24" height="7" fill="var(--violet)"/><rect x="154" y="119" width="36" height="7" fill="var(--red)"/>
    <rect x="86" y="142" width="31" height="7" fill="var(--blue)"/><rect x="117" y="142" width="56" height="7" fill="var(--violet)"/><rect x="173" y="142" width="24" height="7" fill="var(--red)"/>
    <rect x="86" y="165" width="38" height="7" fill="var(--blue)"/><rect x="124" y="165" width="45" height="7" fill="var(--violet)"/><rect x="169" y="165" width="25" height="7" fill="var(--red)"/>
    <g text-anchor="middle">
      <text x="86" y="190">0</text><text x="111.2" y="190">2</text><text x="136.4" y="190">4</text><text x="161.6" y="190">6</text><text x="186.8" y="190">8</text><text x="212" y="190">10</text><text x="237.2" y="190">12</text><text x="262.4" y="190">14</text>
    </g>
    <g stroke="#e4e4e8" stroke-width=".6">
      <line x1="337" y1="88" x2="337" y2="180"/><line x1="382" y1="88" x2="382" y2="180"/><line x1="427" y1="88" x2="427" y2="180"/><line x1="472" y1="88" x2="472" y2="180"/><line x1="517" y1="88" x2="517" y2="180"/>
    </g>
    <g text-anchor="end">
      <text x="331" y="101">Category 4</text><text x="331" y="124">Category 3</text><text x="331" y="147">Category 2</text><text x="331" y="170">Category 1</text>
    </g>
    <rect x="337" y="96" width="40" height="7" fill="var(--blue)"/><rect x="377" y="96" width="23" height="7" fill="var(--violet)"/><rect x="400" y="96" width="42" height="7" fill="var(--red)"/>
    <rect x="337" y="119" width="63" height="7" fill="var(--blue)"/><rect x="400" y="119" width="69" height="7" fill="var(--violet)"/><rect x="469" y="119" width="30" height="7" fill="var(--red)"/>
    <rect x="337" y="142" width="63" height="7" fill="var(--blue)"/><rect x="400" y="142" width="50" height="7" fill="var(--violet)"/><rect x="450" y="142" width="18" height="7" fill="var(--red)"/>
    <rect x="337" y="165" width="74" height="7" fill="var(--blue)"/><rect x="411" y="165" width="62" height="7" fill="var(--violet)"/><rect x="473" y="165" width="18" height="7" fill="var(--red)"/>
    <g text-anchor="middle">
      <text x="337" y="190">0</text><text x="382" y="190">5</text><text x="427" y="190">10</text><text x="472" y="190">15</text><text x="517" y="190">20</text>
    </g>
  </svg>
  <div class="abs" style="left:45px;top:214px;width:225px">
    <div class="item-heading"><b>Heading</b> Goes Here</div>
    <div class="item-text" style="margin-top:5px">Lorem ipsum dolor sit amet, consectetur adipiscing elit. Vivamus eu dui ex. Curabitur dapibus dignissim dui, in molestie metus feugiat sed. Praesent aliquet lorem ex.</div>
  </div>
  <div class="abs" style="left:296px;top:214px;width:225px">
    <div class="item-heading"><b>Heading</b> Goes Here</div>
    <div class="item-text" style="margin-top:5px">Lorem ipsum dolor sit amet, consectetur adipiscing elit. Vivamus eu dui ex. Curabitur dapibus dignissim dui, in molestie metus feugiat sed. Praesent aliquet lorem ex.</div>
  </div>
  <div class="mini-logo">Vantreo</div>
  <div class="footer-bar"><span>Copyright © 2022 Vantreo All rights reserved</span><b class="page-no">8</b></div>
</div>

<!-- Slide 9: table -->
<div class="slide col-a row-5">
  <div class="heading" style="top:26px"><b>Heading</b> Goes Here</div>
  <table class="data-table">
    <thead>
      <tr>
        <th class="first">Heading Goes Here</th>
        <th class="c1">Heading<small>Goes Here</small></th>
        <th class="c2">Heading<small>Goes Here</small></th>
        <th class="c3">Heading<small>Goes Here</small></th>
        <th class="c4">Heading<small>Goes Here</small></th>
      </tr>
    </thead>
    <tbody>
      <tr><td class="name">Lorem ipsum dolor sit amet</td><td class="hi">23</td><td>12</td><td>78</td><td>78</td></tr>
      <tr><td class="name">Vivamus eu dui ex. Curabitur dapibus</td><td class="hi">45</td><td>56</td><td>12</td><td>76</td></tr>
      <tr><td class="name">Praesent aliquet lorem ex, eu dapibus</td><td class="hi">78</td><td>76</td><td>34</td><td>34</td></tr>
      <tr><td class="name">Duis eget tellus porta, consequat lacus</td><td class="hi">22</td><td>12</td><td>55</td><td>67</td></tr>
      <tr><td class="name">Donec risus orci, gravida sit amet</td><td class="hi">34</td><td>66</td><td>45</td><td>11</td></tr>
      <tr><td class="name">Nunc placerat, arcu nec mattis</td><td class="hi">67</td><td>47</td><td>78</td><td>23</td></tr>
      <tr><td class="name">Nam semper tristique mauris</td><td class="hi">87</td><td>67</td><td>12</td><td>45</td></tr>
    </tbody>
  </table>
  <div class="col-highlight"></div>
  <div class="mini-logo">Vantreo</div>
  <div class="footer-bar"><span>Copyright © 2022 Vantreo All rights reserved</span><b class="page-no">9</b></div>
</div>

<!-- Slide 10: thank you -->
<div class="slide col-b row-5">
  <svg class="abs" style="left:0;top:32px" width="563" height="265" viewBox="0 0 563 265" role="img" aria-label="Photo of tall glass office buildings seen from below, tinted purple">
    <polygon points="0,0 430,0 470,48 563,48 563,265 0,265" fill="url(#band-grad)"/>
    <polygon points="300,265 380,40 563,48 563,265" fill="#b08de0" opacity=".25"/>
  </svg>
  <div class="thanks-logo">Vantreo</div>
  <div class="thanks-title">THANK YOU!</div>
  <div class="contact-head">Contact Us</div>
  <ul class="contact-list">
    <li><svg color="#fff"><use href="#i-phone"/></svg>Phone Number Goes Here</li>
    <li><svg color="#fff"><use href="#i-at"/></svg>E-Mail Address Goes Here</li>
    <li><svg color="#fff"><use href="#i-globe"/></svg>URL Address Goes Here</li>
  </ul>
  <div class="slide-copy" style="top:304px">Copyright © 2022 Vantreo All rights reserved</div>
</div>

</body>
</html>
```